KT Fenwick's Brochure - Brevanta Solutions

Hello,
We have an example of very simple brochure (attached below). We would like you to make it better. More sophisticated. More professional looking. All of the info in the document needs to go in the brochure.
Please let me know if you can execute. I will be happy to send over photos, logos etc, once I know.

```html
<!DOCTYPE html>
<html lang="en">
<head>
<meta charset="utf-8">
<title>KT Fenwick's Brochure - Brevanta Solutions</title>
<link rel="stylesheet" href="https://fonts.googleapis.com/css2?family=Bebas+Neue&family=Roboto:wght@400&display=swap">
<style>
  :root {
    --backdrop: #d0d0d0;
    --paper: #ffffff;
    --navy: #2a3a8a;
    --navy-deep: #223178;
    --accent-blue: #2f44a0;
    --grey-tab: #b4b6b9;
    --text-blue: #2d3f96;
    --white: #ffffff;
  }
  html, body {
    margin: 0;
    padding: 0;
    width: 1200px;
    height: 1200px;
    overflow: hidden;
    background: var(--backdrop);
  }
  .spread {
    position: absolute;
    left: 40px;
    top: 205px;
    width: 1120px;
    height: 790px;
    background: var(--paper);
    box-shadow: 0 10px 28px rgba(0,0,0,0.22);
    overflow: hidden;
  }
  .spread-shapes {
    position: absolute;
    inset: 0;
  }
  .heading {
    position: absolute;
    margin: 0;
    font-family: "Bebas Neue", sans-serif;
    font-weight: 400;
    color: var(--white);
    letter-spacing: 1.5px;
  }
  .heading--ribbon {
    left: 24px;
    top: 100px;
    font-size: 37px;
    line-height: 37px;
  }
  .heading--window {
    left: 582px;
    top: 66px;
    font-size: 56px;
    line-height: 56px;
    letter-spacing: 2.5px;
  }
  .intro {
    position: absolute;
    margin: 0;
    font-family: "Roboto", sans-serif;
    color: var(--white);
  }
  .intro--ribbon {
    left: 24px;
    top: 272px;
    width: 232px;
    font-size: 19.5px;
    line-height: 30px;
  }
  .intro--window {
    left: 582px;
    top: 248px;
    width: 226px;
    font-size: 17px;
    line-height: 27px;
  }
  .benefits {
    position: absolute;
    margin: 0;
    padding: 0;
    list-style: none;
    font-family: "Roboto", sans-serif;
    color: var(--text-blue);
  }
  .benefits li {
    position: relative;
    padding-left: 12px;
  }
  .benefits li::before {
    content: "";
    position: absolute;
    left: 0;
    top: 0.55em;
    width: 4px;
    height: 4px;
    background: var(--text-blue);
  }
  .benefits--ribbon {
    left: 24px;
    top: 500px;
    width: 184px;
    font-size: 16.5px;
    line-height: 22.5px;
  }
  .benefits--window {
    left: 582px;
    top: 520px;
    width: 210px;
    font-size: 17px;
    line-height: 24px;
  }
  .brand-tag {
    position: absolute;
    left: 214px;
    top: 16px;
    width: 117px;
    height: 88px;
    background: var(--paper);
    display: flex;
    align-items: center;
    justify-content: center;
    gap: 6px;
    font-family: "Bebas Neue", sans-serif;
    font-size: 30px;
    color: var(--navy);
    letter-spacing: 1px;
  }
  .brand-tag__mark {
    width: 8px;
    height: 8px;
    background: var(--navy);
  }
</style>
</head>
<body>
  <main class="spread">
    <svg class="spread-shapes" width="1120" height="790" viewBox="0 0 1120 790">
      <defs>
        <linearGradient id="blue-photo" x1="0" y1="0" x2="0" y2="1">
          <stop offset="0" stop-color="#5d6db4"/>
          <stop offset="0.55" stop-color="#9aa5d6"/>
          <stop offset="1" stop-color="#4f5fa6"/>
        </linearGradient>
        <linearGradient id="grey-photo" x1="0" y1="0" x2="0" y2="1">
          <stop offset="0" stop-color="#8f9092"/>
          <stop offset="0.6" stop-color="#5e5f61"/>
          <stop offset="1" stop-color="#2c2d2f"/>
        </linearGradient>
        <linearGradient id="grey-photo-light" x1="0" y1="0" x2="0" y2="1">
          <stop offset="0" stop-color="#a9aaad"/>
          <stop offset="1" stop-color="#6d6e71"/>
        </linearGradient>
      </defs>

      <!-- left page: ribbon wall panel -->
      <polygon points="0,0 76,0 0,45" fill="var(--accent-blue)"/>
      <polygon points="0,62 68,27 263,119 263,386 120,467 0,438" fill="var(--navy)"/>
      <polygon points="120,467 263,386 263,467" fill="var(--grey-tab)"/>
      <polygon points="0,760 0,790 40,790" fill="var(--grey-tab)"/>
      <polygon points="187,790 263,753 263,790" fill="var(--accent-blue)"/>

      <!-- left page: photo column -->
      <polygon role="img" aria-label="Photo of a modern office building with white ribbon window bands, tinted blue"
               points="270,126 432,27 557,97 557,386 432,487 270,386" fill="url(#blue-photo)"/>
      <polygon role="img" aria-label="Black and white photo of a brick office building with storefront glazing and a parked car"
               points="270,397 432,498 557,397 557,790 270,790" fill="url(#grey-photo)"/>
      <polygon points="482,0 557,0 557,37" fill="var(--grey-tab)"/>
      <polygon points="485,790 557,752 557,790" fill="var(--accent-blue)"/>

      <!-- right page: window wall panel -->
      <polygon points="557,0 630,0 557,40" fill="var(--accent-blue)"/>
      <polygon points="557,40 630,0 822,0 822,386 697,465 557,386" fill="var(--navy)"/>
      <polygon points="697,465 822,386 822,465" fill="var(--navy-deep)"/>
      <polygon points="557,760 557,790 617,790" fill="var(--grey-tab)"/>
      <polygon points="745,790 822,750 822,790" fill="var(--accent-blue)"/>

      <!-- right page: photo column -->
      <polygon role="img" aria-label="Photo of a tall residential tower with balconies, tinted blue"
               points="832,0 1040,0 1120,50 1120,440 990,492 832,386" fill="url(#blue-photo)"/>
      <polygon role="img" aria-label="Black and white photo of a high-rise apartment tower with a parking podium"
               points="832,397 990,502 1120,452 1120,790 832,790" fill="url(#grey-photo-light)"/>
      <polygon points="1050,0 1120,0 1120,45" fill="var(--grey-tab)"/>
      <polygon points="1020,790 1120,735 1120,790" fill="var(--accent-blue)"/>
    </svg>

    <div class="brand-tag"><span class="brand-tag__mark"></span>FENWICK</div>

    <h2 class="heading heading--ribbon">Unitized<br>Ribbon<br>Wall &amp;<br>Storefront</h2>
    <p class="intro intro--ribbon">Designed for quality and fast installaton. This 2” by 4 1/2” system offers the following benefits:</p>
    <ul class="benefits benefits--ribbon">
      <li>Installed from the interior or exterior</li>
      <li>12 psi water rating</li>
      <li>Higher thermal</li>
      <li>performance due to thermal strut</li>
      <li>Two color option (interior/exterior)</li>
      <li>Larger panes of glass to improve views</li>
      <li>Shipped on metal racks or wood crates</li>
    </ul>

    <h2 class="heading heading--window">Unitized<br>Window<br>Wall</h2>
    <p class="intro intro--window">Designed by installers for an efficient installation with large vision areas. This 6” deep window system offers the following benefits:</p>
    <ul class="benefits benefits--window">
      <li>Punched openings or window wall runs</li>
      <li>Installed from the interior using a receptor system.</li>
      <li>Metal slab covers</li>
      <li>Trim clips are attached</li>
      <li>Shipped on metal racks or wood crates</li>
    </ul>
  </main>
</body>
</html>
```